Business card design for online Mandarin Learning School

We need a business card design for our online language learning school called "Maple Bridge Online for Mandarin Learning". Our existing website is https://www.maplebridgeonline.com
We have our logo already. We would like to see our business card design that can make our online teaching services to be innovative, young, energetic and fun to learn. Prefer to have a certain level of color matching with our website. Apart from "Maple Bridge Online", need to specifically state "for Mandarin Learning" as well on the business card.

```html
<!DOCTYPE html>
<html lang="en">
<head>
<meta charset="utf-8">
<title>Maple Bridge Online – Business Card</title>
<link rel="stylesheet" href="https://fonts.googleapis.com/css2?family=Cinzel:wght@400;500&family=Arimo:wght@400;700&display=swap">
<style>
  :root {
    --bg: #e9e9ec;
    --card: #ffffff;
    --teal: #1fb0b8;
    --coral: #e47c74;
    --grey: #8f8f8f;
    --text: #555555;
    --faint-coral: #fbe6e3;
    --faint-teal: #e6f3f4;
  }
  * { margin: 0; padding: 0; box-sizing: border-box; }
  html, body { width: 1200px; height: 800px; overflow: hidden; }
  body { background: var(--bg); position: relative; font-family: "Arimo", Arial, sans-serif; }

  .card {
    position: absolute;
    width: 525px;
    height: 300px;
    background: var(--card);
    box-shadow: 0 10px 30px rgba(0,0,0,.18);
    overflow: hidden;
  }
  .card--front { left: 50px; top: 250px; display: flex; align-items: center; justify-content: center; gap: 16px; }
  .card--back { left: 625px; top: 250px; }

  .brand-dot { width: 22px; height: 22px; border-radius: 50%; background: var(--coral); flex: none; }
  .brand-text { display: flex; flex-direction: column; align-items: flex-start; }
  .brand-name {
    font-family: "Cinzel", "Times New Roman", serif;
    font-weight: 400;
    font-size: 38px;
    line-height: 1.1;
    letter-spacing: 2px;
    color: var(--teal);
  }
  .brand-tagline {
    font-family: "Cinzel", "Times New Roman", serif;
    font-weight: 400;
    font-size: 15px;
    letter-spacing: 2px;
    color: var(--grey);
    margin-top: 4px;
  }

  .side-band { position: absolute; left: 0; top: 0; width: 120px; height: 300px; }

  .faint-decoration {
    position: absolute; right: -40px; top: -30px; width: 330px; height: 330px;
    background: radial-gradient(circle at 40% 40%, var(--faint-coral) 0%, var(--faint-teal) 55%, rgba(255,255,255,0) 72%);
  }

  .accent-line {
    position: absolute; left: 280px; top: 60px; width: 230px; height: 1.5px;
    background: var(--coral); transform-origin: left center; transform: rotate(-10deg);
  }

  .contact { position: absolute; left: 150px; top: 40px; color: var(--text); }
  .contact__name { font-weight: 700; font-size: 21px; color: var(--teal); }
  .contact__role { font-size: 13px; color: var(--grey); margin-bottom: 22px; }
  .contact__address { font-size: 13px; line-height: 1.35; margin-bottom: 16px; }
  .contact__list { list-style: none; font-size: 13px; line-height: 1.65; }
  .contact__list li { display: flex; align-items: center; gap: 8px; }
  .contact__web { color: var(--teal); }
  .icon { width: 16px; height: 16px; flex: none; }
</style>
</head>
<body>

  <section class="card card--front">
    <span class="brand-dot"></span>
    <div class="brand-text">
      <span class="brand-name">MAPLE BRIDGE</span>
      <span class="brand-tagline">ONLINE for Mandarin Learning</span>
    </div>
  </section>

  <section class="card card--back">
    <div class="faint-decoration" role="img" aria-label="Soft faint brand colour wash"></div>

    <svg class="side-band" viewBox="0 0 120 300" aria-label="Brand band">
      <rect x="0" y="0" width="42" height="60" fill="#8f8f8f"/>
      <rect x="0" y="60" width="42" height="50" fill="#e47c74"/>
      <rect x="0" y="110" width="42" height="70" fill="#8f8f8f"/>
      <rect x="0" y="180" width="42" height="50" fill="#1fb0b8"/>
      <rect x="0" y="230" width="42" height="70" fill="#8f8f8f"/>
      <rect x="42" y="0" width="78" height="50" fill="#e47c74"/>
      <rect x="42" y="50" width="78" height="60" fill="#1fb0b8"/>
      <rect x="42" y="110" width="78" height="60" fill="#e47c74"/>
      <rect x="42" y="170" width="78" height="60" fill="#8f8f8f"/>
      <rect x="42" y="230" width="78" height="70" fill="#1fb0b8"/>
      <line x1="44" y1="0" x2="44" y2="300" stroke="#fff" stroke-width="2"/>
      <text x="-150" y="26" transform="rotate(-90)" text-anchor="middle" fill="#fff"
            font-family="Cinzel, serif" font-size="11" letter-spacing="1.5">WWW.MAPLEBRIDGEONLINE.COM</text>
      <text x="-150" y="93" transform="rotate(-90)" text-anchor="middle" fill="#fff"
            font-family="Cinzel, serif" font-size="30" letter-spacing="1">MAPLE BRIDGE</text>
    </svg>

    <div class="accent-line"></div>

    <div class="contact">
      <p class="contact__name">Liam Carter</p>
      <p class="contact__role">Manager</p>
      <p class="contact__address">PO BOX 456, your address<br>5th street Brisbane<br>Australia</p>
      <ul class="contact__list">
        <li>
          <svg class="icon" viewBox="0 0 16 16"><circle cx="8" cy="8" r="8" fill="#e47c74"/><path d="M5.5 4.5l1.5 0 .6 2-1 .8a5 5 0 0 0 2.1 2.1l.8-1 2 .6v1.5c0 .5-.5 1-1 1A6.5 6.5 0 0 1 4.5 5.5c0-.5.5-1 1-1z" fill="#fff"/></svg>
          <span>555.010.2020</span>
        </li>
        <li>
          <svg class="icon" viewBox="0 0 16 16"><circle cx="8" cy="8" r="8" fill="#1fb0b8"/><rect x="4" y="5" width="8" height="6" rx="1" fill="#fff"/><path d="M4.3 5.4L8 8.3l3.7-2.9" stroke="#1fb0b8" fill="none" stroke-width=".9"/></svg>
          <span>hello@maplebridgemail.com</span>
        </li>
        <li>
          <svg class="icon" viewBox="0 0 16 16"><circle cx="8" cy="8" r="8" fill="#e47c74"/><circle cx="8" cy="8" r="4" fill="none" stroke="#fff" stroke-width="1"/><path d="M4 8h8M8 4v8" stroke="#fff" stroke-width=".8"/></svg>
          <span>www.<span class="contact__web">maplebridgeonline</span>.com</span>
        </li>
      </ul>
    </div>
  </section>

</body>
</html>
```